Our architectural studio needs a new business card

We need a business card design for our studio based in Waterloo in Belgium. We are active in architecture, design and installation.
Our works are contemporary and minimalist. our clients are refined and cultured.
Our business card must be minimalist and refined.

Project Deadline Extended
Reason: Some designers have accepted my invitation but they don't have all replied. I want to give them a chance to make one proposal. Paul

Target Market(s)

architecture

Industry/Entity Type

Business

Contact Information for Business Card

studio: paul dornevaux studio
paul dornevaux, architecte
M. +32 471 586 927
F. +322 619 4850
www.pauldornevaux-example.com
paul@pauldornevaux-example.com
14 rue des Marronniers
1420 Waterloo
Belgium

Font styles to use
Sans Serif

Requirements
Must have
• simple, minimalist, clear, elegant and chic! Black and white
Nice to have
• embossed logo, other format like a square for example
Should not have
• color, fantasy, curves, ...

```html
<!DOCTYPE html>
<html lang="fr">
<head>
<meta charset="utf-8">
<title>Paul Dornevaux Studio — cartes de visite</title>
<link href="https://fonts.googleapis.com/css2?family=Lato:wght@400;700&display=swap" rel="stylesheet">
<style>
  :root {
    --page-bg: #e6e2df;
    --card-black: #1f1f20;
    --card-white: #fdfdfd;
    --ink: #1c1c1c;
    --ink-soft: #2a2a2a;
    --paper-ink: #ffffff;
    --ghost: #ececec;
    --rule: #d9d9d9;
  }
  * { margin: 0; padding: 0; box-sizing: border-box; }
  html, body { width: 1200px; height: 720px; overflow: hidden; }
  body {
    background: var(--page-bg);
    font-family: "Lato", sans-serif;
    position: relative;
  }
  .card {
    position: absolute;
    top: 232px;
    width: 451px;
    height: 257px;
    overflow: hidden;
  }
  .card--front { left: 114px; background: var(--card-black); color: var(--paper-ink); }
  .card--back  { left: 635px; background: var(--card-white); color: var(--ink); }

  /* front */
  .front-mark {
    position: absolute;
    left: 50%;
    top: 62px;
    width: 52px;
    height: 52px;
    margin-left: -26px;
    background: var(--paper-ink);
  }
  .front-studio {
    position: absolute;
    left: 0; right: 0;
    top: 188px;
    text-align: center;
    font-size: 11px;
    font-weight: 700;
    letter-spacing: 2.6px;
    text-transform: uppercase;
  }

  /* back */
  .back-ghost-square {
    position: absolute;
    left: 18px;
    top: 14px;
    width: 96px;
    height: 96px;
    background: var(--ghost);
  }
  .back-divider-v {
    position: absolute;
    left: 123px;
    top: 0;
    width: 1px;
    height: 146px;
    background: var(--rule);
  }
  .back-mark {
    position: absolute;
    right: 22px;
    top: 22px;
    width: 30px;
    height: 30px;
    background: var(--ink);
  }
  .back-studio {
    position: absolute;
    right: 22px;
    top: 124px;
    font-size: 9px;
    font-weight: 700;
    letter-spacing: 2.2px;
    text-transform: uppercase;
  }
  .back-rule {
    position: absolute;
    left: 0; right: 0;
    top: 146px;
    height: 1.5px;
    background: var(--ink);
  }
  .person {
    position: absolute;
    left: 22px;
    top: 156px;
    font-size: 13px;
    color: var(--ink-soft);
  }
  .person strong { font-weight: 700; color: var(--ink); }
  .phones {
    position: absolute;
    left: 22px;
    top: 192px;
    list-style: none;
    font-size: 12px;
    line-height: 16px;
  }
  .phones li { display: flex; align-items: center; gap: 4px; }
  .phones svg { width: 9px; height: 9px; fill: var(--ink); }
  .contact {
    position: absolute;
    right: 22px;
    top: 178px;
    text-align: right;
    font-style: normal;
    font-size: 11.5px;
    line-height: 15.5px;
  }
</style>
</head>
<body>
  <section class="card card--front" aria-label="Recto">
    <div class="front-mark"></div>
    <p class="front-studio">Paul Dornevaux Studio</p>
  </section>

  <section class="card card--back" aria-label="Verso">
    <div class="back-ghost-square"></div>
    <div class="back-divider-v"></div>
    <div class="back-mark"></div>
    <p class="back-studio">Paul Dornevaux Studio</p>
    <div class="back-rule"></div>

    <p class="person"><strong>Paul Dornevaux</strong> / Architecte</p>

    <ul class="phones">
      <li>
        <svg viewBox="0 0 10 10" aria-hidden="true"><path d="M2 0.5 L3.6 0.5 L4.2 2.8 L3 3.7 C3.6 5 4.9 6.4 6.3 7 L7.2 5.8 L9.5 6.4 L9.5 8 C9.5 9 8.7 9.5 8 9.5 C3.8 9.2 0.8 6.2 0.5 2 C0.5 1.2 1 0.5 2 0.5 Z"/></svg>
        +32 471 586 927
      </li>
      <li>
        <svg viewBox="0 0 10 10" aria-hidden="true"><rect x="2.5" y="0.5" width="5" height="3"/><rect x="0.5" y="3.5" width="9" height="4" rx="0.6"/><rect x="2.5" y="6.5" width="5" height="3" fill="#fff" stroke="#1c1c1c" stroke-width="0.8"/></svg>
        +322 619 4850
      </li>
    </ul>

    <address class="contact">
      paul@pauldornevaux-example.com<br>
      www.pauldornevaux-example.com<br>
      14 rue des Marronniers 1420<br>
      Waterloo Belgium
    </address>
  </section>
</body>
</html>
```